Business card for a "family office" company

Please provide professional looking business card designs, incorporating the attached logo and below details. Harrowmere Holdings Pty Ltd is a family office / financial investment company. We are looking for a modern, professional and contemporary card design.

Industry/Entity Type

Finance

Contact Information for Business Card

Name: Dean Malcott
Title: Director
Company: Harrowmere Holdings Pty Ltd
Email: harrowlead@ozmailnet.com.au
Mobile: 0492 635 718
Address: 3/412 Bramwood Parade, Kellerton WA 6158, Australia

Requirements
Must have
• All details above and the logo. logo only on back side. incorporate colours of logo
Nice to have
• up to you
Should not have
• ?

```html
<!DOCTYPE html>
<html lang="en">
<head>
<meta charset="utf-8">
<title>Harrowmere Holdings – Business Card</title>
<link href="https://fonts.googleapis.com/css2?family=Cinzel:wght@500;700&family=Didact+Gothic&display=swap" rel="stylesheet">
<style>
  :root {
    --navy: #1f1e66;
    --navy-deep: #19185a;
    --paper: #ffffff;
    --ink: #1f1e66;
    --muted: #555566;
    --contact: #2a2a3a;
    --backdrop: #e4e4e6;
  }
  * { margin: 0; padding: 0; box-sizing: border-box; }
  html, body { width: 1200px; height: 1000px; overflow: hidden; }
  body { background: var(--backdrop); position: relative; font-family: "Didact Gothic", sans-serif; }

  .card {
    position: absolute;
    width: 630px;
    height: 360px;
    border-radius: 4px;
    box-shadow: 0 10px 30px rgba(0,0,0,0.18);
    overflow: hidden;
  }

  /* Back side */
  .card--back {
    left: 90px;
    top: 90px;
    background: var(--navy);
    display: flex;
    align-items: center;
    justify-content: center;
  }
  .wordmark {
    display: flex;
    align-items: center;
    gap: 14px;
    font-family: "Cinzel", serif;
    font-weight: 500;
    letter-spacing: 2px;
    white-space: nowrap;
  }
  .wordmark__mark { width: 18px; height: 18px; }
  .card--back .wordmark { color: var(--paper); font-size: 30px; }
  .card--back .wordmark__mark { background: var(--paper); }

  /* Front side */
  .card--front {
    left: 480px;
    top: 550px;
    background: var(--paper);
  }
  .card--front .wordmark {
    position: absolute;
    right: 36px;
    top: 48px;
    color: var(--ink);
    font-size: 22px;
    gap: 10px;
  }
  .card--front .wordmark__mark { background: var(--ink); width: 14px; height: 14px; }

  .holder {
    position: absolute;
    left: 40px;
    top: 150px;
  }
  .holder__name {
    font-family: "Cinzel", serif;
    font-weight: 700;
    font-size: 30px;
    color: var(--ink);
    letter-spacing: 1px;
    line-height: 1;
    white-space: nowrap;
  }
  .holder__title {
    font-family: "Cinzel", serif;
    font-weight: 500;
    font-size: 15px;
    color: var(--muted);
    letter-spacing: 1px;
    margin-top: 4px;
  }

  .contacts {
    position: absolute;
    left: 44px;
    top: 232px;
    list-style: none;
  }
  .contacts li {
    display: flex;
    align-items: center;
    gap: 10px;
    font-size: 15px;
    color: var(--contact);
    line-height: 24px;
    letter-spacing: 0.4px;
    white-space: nowrap;
  }
  .contacts svg { width: 13px; height: 13px; fill: var(--ink); flex: none; }

  .address {
    position: absolute;
    right: 36px;
    top: 152px;
    text-align: right;
    font-size: 13px;
    color: var(--contact);
    line-height: 18px;
    letter-spacing: 0.3px;
    white-space: nowrap;
  }

  .front-band { position: absolute; left: 0; bottom: 0; width: 630px; height: 40px; }
</style>
</head>
<body>

  <section class="card card--back" aria-label="Card back">
    <div class="wordmark">
      <span class="wordmark__mark"></span>
      <span class="wordmark__name">Harrowmere Holdings</span>
    </div>
  </section>

  <section class="card card--front" aria-label="Card front">
    <div class="wordmark">
      <span class="wordmark__mark"></span>
      <span class="wordmark__name">Harrowmere Holdings</span>
    </div>

    <div class="holder">
      <p class="holder__name">DEAN MALCOTT</p>
      <p class="holder__title">DIRECTOR</p>
    </div>

    <ul class="contacts">
      <li>
        <svg viewBox="0 0 24 24" aria-hidden="true"><path d="M6.6 10.8a15 15 0 0 0 6.6 6.6l2.2-2.2a1 1 0 0 1 1-.25 11.4 11.4 0 0 0 3.6.57 1 1 0 0 1 1 1V20a1 1 0 0 1-1 1A17 17 0 0 1 3 4a1 1 0 0 1 1-1h3.5a1 1 0 0 1 1 1c0 1.25.2 2.45.57 3.570a1 1 0 0 1-.25 1z"/></svg>
        0492 635 718
      </li>
      <li>
        <svg viewBox="0 0 24 24" aria-hidden="true"><path d="M2 5h20v14H2z"/><path d="M2 5h20L12 13z" fill="#fff"/></svg>
        harrowlead@ozmailnet.com.au
      </li>
      <li>
        <svg viewBox="0 0 24 24" aria-hidden="true"><path d="M12 2a10 10 0 1 0 0 20 10 10 0 0 0 0-20zm6.9 6h-2.9a15 15 0 0 0-1.4-3.6A8 8 0 0 1 18.9 8zM12 4c.8 1.2 1.5 2.5 1.9 4h-3.8c.4-1.5 1.1-2.8 1.9-4zM4.3 14a8 8 0 0 1 0-4h3.4a16 16 0 0 0 0 4zm.8 2h2.9a15 15 0 0 0 1.4 3.6A8 8 0 0 1 5.1 16zM8 8H5.1a8 8 0 0 1 4.3-3.6A15 15 0 0 0 8 8zm4 12c-.8-1.2-1.5-2.5-1.9-4h3.8c-.4 1.5-1.1 2.8-1.9 4zm2.3-6H9.7a14 14 0 0 1 0-4h4.6a14 14 0 0 1 0 4zm.3 5.6A15 15 0 0 0 16 16h2.9a8 8 0 0 1-4.3 3.6zm1.7-5.6a16 16 0 0 0 0-4h3.4a8 8 0 0 1 0 4z"/></svg>
        www.harrowmereholdings.com.au
      </li>
    </ul>

    <p class="address">3/412 Bramwood Parade,<br>Kellerton WA 6158, Australia</p>

    <svg class="front-band" viewBox="0 0 630 40" preserveAspectRatio="none" aria-hidden="true">
      <path d="M0 40 L0 32 Q330 26 630 0 L630 40 Z" fill="var(--navy-deep)"/>
    </svg>
  </section>

</body>
</html>
```